Small property developments

I'm just starting out developing duplex homes on urban infill sites in the Brackwood City Council region of Brisbane. I need a business card to give to planners, engineers and builders. I was thinking of a logo that showed two homes under a single roof which is what a duplex is, but all good development and construction themes considered. Company name will be Marty Loft Developments.

```html
<!DOCTYPE html>
<html lang="en">
<head>
<meta charset="utf-8">
<title>Marty Loft Development – Business Card</title>
<link rel="stylesheet" href="https://fonts.googleapis.com/css2?family=Cinzel:wght@500&family=Open+Sans:wght@400;700&family=Pathway+Gothic+One&display=swap">
<style>
  :root {
    --plum: #922a8f;
    --plum-deep: #7a1f78;
    --plum-soft: #d9b3d8;
    --ring: rgba(255, 255, 255, 0.32);
    --paper: #ffffff;
    --ink: #111111;
    --backdrop: #ffffff;
  }
  * { box-sizing: border-box; margin: 0; padding: 0; }
  html, body {
    width: 857px; height: 1200px; overflow: hidden;
    background: var(--backdrop);
  }
  .sheet { position: relative; width: 857px; height: 1200px; }

  .side-label {
    position: absolute; left: 0; width: 100%;
    text-align: center;
    font-family: "Open Sans", sans-serif; font-weight: 700;
    font-size: 40px; color: var(--ink);
  }
  .side-label--front { top: 48px; }
  .side-label--back { top: 610px; }

  .card {
    position: absolute; left: 88px;
    width: 680px; height: 380px; overflow: hidden;
  }
  .card--front { top: 120px; background: var(--plum); color: var(--paper); }
  .card--back { top: 690px; background: var(--paper); border: 2px solid var(--plum); color: var(--plum); }

  .card__rings { position: absolute; inset: 0; }

  .wordmark {
    position: absolute;
    font-family: "Pathway Gothic One", sans-serif;
    font-size: 64px; line-height: 1;
  }
  .card--front .wordmark { left: 44px; top: 34px; }
  .card--back .wordmark { left: 286px; top: 120px; color: var(--plum); }

  .company {
    position: absolute;
    font-family: "Cinzel", serif; font-weight: 500;
    font-size: 32px; letter-spacing: 0.5px; white-space: nowrap;
  }
  .slogan {
    position: absolute;
    font-family: "Open Sans", sans-serif; font-weight: 700;
    font-size: 21px; white-space: nowrap;
  }
  .card--front .company { left: 0; width: 100%; text-align: center; top: 122px; }
  .card--front .slogan { left: 0; width: 100%; text-align: center; top: 168px; }
  .card--back .company { left: 120px; top: 200px; }
  .card--back .slogan { left: 260px; top: 242px; color: var(--plum-deep); }

  .contact {
    position: absolute; top: 288px;
    font-family: "Open Sans", sans-serif; font-size: 15px; line-height: 1.6;
  }
  .contact--left { left: 46px; }
  .contact--right { right: 46px; text-align: right; }
  .contact__divider {
    position: absolute; left: 296px; top: 286px;
    width: 2px; height: 40px; background: var(--paper);
  }
</style>
</head>
<body>
<main class="sheet">
  <h2 class="side-label side-label--front">Front side</h2>
  <section class="card card--front" aria-label="Business card front">
    <svg class="card__rings" width="680" height="380" viewBox="0 0 680 380" aria-hidden="true">
      <g fill="none" stroke="var(--ring)" stroke-width="14">
        <circle cx="518" cy="118" r="92"/>
        <circle cx="450" cy="248" r="86"/>
        <circle cx="578" cy="254" r="86"/>
      </g>
    </svg>
    <div class="wordmark">Logo</div>
    <div class="company">Marty Loft Development</div>
    <div class="slogan">slogan slogan slogan</div>
    <div class="contact contact--left">Phone #<br>Address:</div>
    <div class="contact__divider"></div>
    <div class="contact contact--right">Fax #<br>www.martyloftdevelopment.com</div>
  </section>

  <h2 class="side-label side-label--back">Back side</h2>
  <section class="card card--back" aria-label="Business card back">
    <svg class="card__rings" width="680" height="380" viewBox="0 0 680 380" aria-hidden="true">
      <circle cx="50" cy="92" r="96" fill="none" stroke="var(--plum-soft)" stroke-width="16"/>
    </svg>
    <div class="wordmark">Logo</div>
    <div class="company">Marty Loft Development</div>
    <div class="slogan">slogan slogan slogan</div>
  </section>
</main>
</body>
</html>
```